Auto Mechanic business card

Need a general business card for GearFixer.
Name on card should be 'Roadside Wrench'
Tel # (555) 412 3097
Address is - Palm Lane, Harbourton, Coral Isle
Whatsapp and facebook symbols should be added
On back of card should include services offered
General Repairs
Brakes
Tune Ups
Suspensions
Oil Leaks
Dent repairs
Suspensions
Car Sales
Tyre Repairs
General service
Check Engine Light
Minor Electricals

Target Market(s)

General Population, University students

Industry/Entity Type

Auto Mechanic

Contact Information for Business Card

Roadside Wrench

Requirements
Must have
• 2 Sides

```html
<!DOCTYPE html>
<html lang="en">
<head>
<meta charset="utf-8">
<title>GearFixer – Business Card</title>
<link rel="stylesheet" href="https://fonts.googleapis.com/css2?family=Michroma&family=Oswald:wght@400;500&display=swap">
<style>
  :root {
    --page: #d3d3d3;
    --ink: #000000;
    --blue: #1a74c6;
    --white: #ffffff;
    --text-dark: #111111;
    --shadow: rgba(0,0,0,0.35);
  }
  * { box-sizing: border-box; margin: 0; padding: 0; }
  html, body { width: 1084px; height: 1200px; overflow: hidden; background: var(--page); }
  .canvas { position: relative; width: 1084px; height: 1200px; }

  .card {
    position: absolute; left: 122px; width: 840px; height: 480px;
    box-shadow: 0 4px 10px var(--shadow); overflow: hidden;
  }
  .card--front { top: 90px; }
  .card--back { top: 630px; background: var(--ink); }
  .card__shapes { position: absolute; inset: 0; width: 100%; height: 100%; }

  .brand {
    position: absolute; left: 0; right: 0; text-align: center;
    font-family: "Michroma", sans-serif; font-size: 46px; letter-spacing: 2px;
    color: var(--white); text-transform: uppercase; white-space: nowrap;
  }
  .card--front .brand { top: 58px; }
  .card--back .brand { top: 60px; }

  .car-visual { position: absolute; right: 0; top: 0; width: 300px; height: 182px;
    background: radial-gradient(ellipse at 60% 60%, #1c1c1c 0%, #0a0a0a 55%, #000 100%); }
  .car-visual--back { left: 260px; top: 200px; width: 340px; height: 260px; right: auto;
    background: radial-gradient(ellipse at 50% 55%, #151515 0%, #050505 60%, #000 100%); }

  .holder {
    position: absolute; left: 0; right: 0; text-align: center; color: var(--text-dark); white-space: nowrap;
  }
  .holder__name { top: 256px; font-family: "Michroma", sans-serif; font-size: 30px; font-weight: 400; letter-spacing: 1px; text-transform: uppercase; }
  .holder__line { font-family: "Oswald", sans-serif; font-size: 27px; text-transform: uppercase; }
  .holder__address { top: 312px; }
  .holder__phone { top: 356px; }

  .services {
    position: absolute; top: 166px; list-style: none;
    font-family: "Oswald", sans-serif; font-size: 28px; line-height: 42.5px;
    color: var(--white); text-transform: uppercase; white-space: nowrap;
  }
  .services--left { left: 166px; }
  .services--right { left: 456px; }
  .services li { display: flex; align-items: center; gap: 14px; }
  .services li::before {
    content: ""; width: 12px; height: 12px; border: 3px solid var(--blue);
    border-radius: 50%; flex: none;
  }

  .contact {
    position: absolute; top: 422px; display: flex; align-items: center; gap: 12px;
    font-family: "Oswald", sans-serif; font-size: 29px; color: var(--white); text-transform: uppercase; white-space: nowrap;
  }
  .contact--phone { left: 46px; }
  .contact--social { left: 614px; }
  .contact__dot { width: 30px; height: 30px; border-radius: 50%; background: var(--blue); flex: none; }
</style>
</head>
<body>
<main class="canvas">

  <section class="card card--front" aria-label="Card front">
    <svg class="card__shapes" viewBox="0 0 840 480" preserveAspectRatio="none" aria-hidden="true">
      <defs>
        <linearGradient id="paperShade" x1="0" y1="0" x2="0" y2="1">
          <stop offset="0" stop-color="#ececec"/>
          <stop offset="1" stop-color="#e2e2e2"/>
        </linearGradient>
      </defs>
      <rect width="840" height="480" fill="url(#paperShade)"/>
      <rect width="840" height="182" fill="#000"/>
      <polygon points="0,166 464,166 476,176 0,176" fill="#1a74c6"/>
      <rect y="446" width="840" height="34" fill="#000"/>
      <polygon points="372,446 840,446 840,456 384,456" fill="#1a74c6"/>
    </svg>
    <div class="car-visual" role="img" aria-label="Faint photo of a car front, fading into black"></div>
    <div class="brand">GearFixer</div>
    <h1 class="holder holder__name">Roadside Wrench</h1>
    <p class="holder holder__line holder__address">Palm Lane, Harbourton, Coral Isle</p>
    <p class="holder holder__line holder__phone">(555) 412 3097</p>
  </section>

  <section class="card card--back" aria-label="Card back">
    <div class="car-visual car-visual--back" role="img" aria-label="Faint photo of a car behind the services list"></div>
    <div class="brand">GearFixer</div>
    <ul class="services services--left">
      <li>General Repairs</li>
      <li>Brakes</li>
      <li>Tune Ups</li>
      <li>Suspensions</li>
      <li>Oil Leaks</li>
      <li>Dent Repairs</li>
    </ul>
    <ul class="services services--right">
      <li>Suspensions</li>
      <li>Car Sales</li>
      <li>Tyre Repairs</li>
      <li>General Service</li>
      <li>Check Engine Light</li>
      <li>Minor Electricals</li>
    </ul>
    <p class="contact contact--phone"><span class="contact__dot" aria-hidden="true"></span>029 555 0147</p>
    <p class="contact contact--social"><span class="contact__dot" aria-hidden="true"></span>YourFBLink</p>
  </section>

</main>
</body>
</html>
```